SOLVEN TRIDE PORTAL

I'D LIKE TO REDESIGN MY WEBSITE TO MATCH WITH THE NEW BROCHURE WHICH IS ATTACHED. CONTENT AND LOGOS ARE ATTACHED. PLEASE USE WATCH BRAND LOGOS FROM THE BROCHURE
Coded - Design and coding required
1 page

```html
<!DOCTYPE html>
<html lang="en">
<head>
<meta charset="utf-8">
<title>Solven Tride Portal — International Luxury Timepiece Supplier</title>
<link href="https://fonts.googleapis.com/css2?family=Poppins:wght@300;400;500;600;700&display=swap" rel="stylesheet">
<style>
:root{
  --black:#000;
  --gold:#c29d3d;
  --gold-text:#c9a12e;
  --gold-bright:#e6c94a;
  --yellow:#e8da62;
  --cream:#ede48e;
  --ink:#1d1d1d;
  --grey:#5c5c5c;
  --navy:#0d1a2b;
  --footer:#fcfbf5;
  --white:#fff;
}
*{box-sizing:border-box;margin:0;padding:0}
html,body{width:1200px;height:3477px;overflow:hidden}
body{font-family:'Poppins',sans-serif;color:var(--ink);background:var(--white);position:relative}
.abs{position:absolute}

/* header */
.site-header{position:absolute;left:0;top:0;width:1200px;height:89px;background:var(--black);border-bottom:2px solid #555}
.brand{position:absolute;display:flex;align-items:center;gap:6px;color:var(--gold);font-weight:600;font-size:10px;letter-spacing:.5px}
.brand-mark{width:10px;height:10px;background:var(--gold)}
.site-header .brand{left:128px;top:38px}
.main-nav{position:absolute;left:376px;top:34px;display:flex;gap:43px}
.main-nav a{color:var(--white);text-decoration:none;font-size:14.5px;letter-spacing:.3px}
.main-nav a.active{color:var(--gold-bright);font-weight:600;border-bottom:2px solid var(--gold-bright);padding-bottom:8px}
.header-cta{position:absolute;left:938px;top:24px;width:132px;height:39px;background:var(--yellow);color:var(--black);font-weight:600;font-size:14px;display:flex;align-items:center;justify-content:center}

/* hero */
.hero{position:absolute;left:0;top:89px;width:1200px;height:592px;background:linear-gradient(100deg,#050505 0%,#1a1310 40%,#5c3d2e 65%,#8d6f62 85%,#3a2a25 100%)}
.hero-copy{position:absolute;left:106px;top:156px;width:640px;color:var(--white)}
.hero-copy h1{font-size:30px;font-weight:500;line-height:43px;letter-spacing:.3px}
.hero-copy h1 strong{font-weight:600}
.hero-copy p{font-size:13.5px;font-weight:500;line-height:28px;margin-top:22px}
.hero-copy .tagline{font-size:18px;font-weight:400;margin-top:20px}
.dots{position:absolute;left:566px;top:525px;display:flex;gap:10px}
.dots span{width:16px;height:16px;border-radius:50%;background:var(--white)}

/* about */
.about-photo{position:absolute;left:108px;top:806px;width:426px;height:367px;border:12px solid var(--gold);outline:2px solid #e3cc7a;outline-offset:3px;background:radial-gradient(circle at 60% 55%,#6d6d6d,#1b1b1b 70%)}
.section-title{font-size:35px;font-weight:400;letter-spacing:.5px}
.about-copy{position:absolute;left:613px;top:756px;width:520px}
.about-copy p{font-size:14px;color:var(--grey);line-height:25.6px;margin-top:12px}
.about-copy .section-title{color:var(--ink);margin-bottom:4px}
.outline-btn{position:absolute;display:flex;align-items:center;justify-content:center;font-weight:600;font-size:14px}
.about-cta{left:614px;top:1210px;width:132px;height:38px;border:2px solid var(--gold);color:var(--gold)}

/* investments */
.investments{position:absolute;left:0;top:1345px;width:1200px;height:585px;background:radial-gradient(circle at 80% 45%,#2d5870 0%,#12273a 30%,var(--navy) 60%,#060d17 100%)}
.investments-copy{position:absolute;left:166px;top:172px;width:520px;color:var(--white)}
.investments-copy h2{color:var(--gold-bright);font-size:36px;font-weight:500;letter-spacing:.5px}
.investments-copy p{font-size:16px;line-height:26px;margin-top:10px}
.invest-cta{left:168px;top:362px;width:142px;height:38px;border:2px solid var(--gold-bright);color:var(--gold-bright)}

/* sourcing */
.sourcing-title{position:absolute;left:0;top:2012px;width:1200px;text-align:center;color:var(--ink)}
.filter{position:absolute;width:312px;height:54px;background:var(--yellow);display:flex;align-items:center;justify-content:space-between;padding:0 24px 0 28px;font-size:17px;letter-spacing:.3px}
.filter svg{width:18px;height:12px}
.source-cta{left:535px;top:2233px;width:131px;height:39px;border:2px solid var(--ink);color:var(--ink);font-size:14px}

/* contact */
.contact{position:absolute;left:0;top:2380px;width:1200px;height:686px;background:var(--cream)}
.contact-copy{position:absolute;left:157px;top:145px;width:460px}
.contact-copy .section-title{font-size:36px}
.contact-copy p{font-size:14px;color:#444;line-height:26px}
.contact-copy .intro{margin-top:14px}
.info-row{position:absolute;left:154px;display:flex;gap:14px}
.info-row .ic{width:50px;height:50px;border-radius:50%;background:var(--gold);display:flex;align-items:center;justify-content:center}
.info-row b{display:block;font-weight:400;font-size:19px;color:#222}
.info-row span{font-size:17px;color:#5f6b7a}
.contact-form{position:absolute;left:634px;top:61px;width:437px;height:550px;background:var(--gold)}
.field{position:absolute;left:46px;width:336px;height:54px;background:var(--white);font-size:17px;color:#333;padding:14px 14px}
.submit{left:49px;top:467px;width:148px;height:38px;border:2px solid #222;color:#222;font-size:14px}

/* footer */
.site-footer{position:absolute;left:0;top:3066px;width:1200px;height:349px;background:var(--footer)}
.footer-brand{position:absolute;left:130px;top:94px;display:flex;align-items:center;gap:6px;color:var(--gold);font-weight:600;font-size:12px;letter-spacing:.5px}
.socials{position:absolute;left:132px;top:242px;display:flex;gap:16px}
.socials span{width:31px;height:31px;border-radius:50%;background:var(--gold)}
.footer-col{position:absolute;top:88px;padding-left:18px;border-left:3px solid var(--gold)}
.footer-col h4{font-size:17px;font-weight:600;color:#1e2a44}
.footer-col ul{list-style:none;margin-top:10px}
.footer-col li{font-size:14px;color:#555;line-height:29px}
.divider{position:absolute;top:50px;width:1px;height:170px;background:#eee}
.fc-row{position:absolute;left:876px;display:flex;align-items:center;gap:12px;font-size:12px;color:#555}
.fc-row .ic{width:32px;height:32px;border-radius:50%;background:var(--gold);display:flex;align-items:center;justify-content:center}
.copyright{position:absolute;left:0;top:3415px;width:1200px;height:62px;border-top:1px solid #ddd;background:var(--footer);text-align:center;font-size:10.5px;color:#999;padding-top:24px}
</style>
</head>
<body>

<header class="site-header">
  <div class="brand"><span class="brand-mark"></span>SOLVEN TRIDE PORTAL</div>
  <nav class="main-nav">
    <a class="active" href="#">HOME</a><a href="#">ABOUT US</a><a href="#">INVESTMENTS</a><a href="#">SEARCH WATCHES</a>
  </nav>
  <div class="header-cta">CONTACT US</div>
</header>

<section class="hero" role="img" aria-label="Hand adjusting a luxury wristwatch on a suited wrist">
  <div class="hero-copy">
    <h1>WELCOME TO SOLVEN TRIDE PORTAL<br><strong>INTERNATIONAL LUXURY TIMEPIECE SUPPLIER</strong></h1>
    <p>Simply choose a desired product and allow us to source it for you at the best price and with suitable delivery terms. You will have an option to either collect your purchase from our Cheshire based boutique store, collection points are also in New York City or Dubai or get it delivered to your door via one of our fully insured couriers.</p>
    <p class="tagline">Making your luxury shopping experience as simple as it can be.</p>
  </div>
  <div class="dots"><span></span><span></span><span></span></div>
</section>

<div class="about-photo" role="img" aria-label="Close-up of a black luxury watch dial in a gold frame"></div>
<section class="about-copy">
  <h2 class="section-title">ABOUT US</h2>
  <p>Solven Tride Portal was first founded in 2018, it has been established as the premier resource to buy and sell premium pre-owned watches. With thousands of watches available from brands including Varnholt, Marcel Orvain, Lessard Quintel, Tobias Renn, Halvora, Bellamort and more, plus international locations and clients there's no better place to find a luxury timepiece.</p>
  <p>Outstanding customer service is a mainstay of the Solven Tride ethos. Watch collectors are discerning shoppers, and will accept nothing but the best, which is why customer service has and always will be such an important part of the business.</p>
  <p>Our dedicated team of swiss watch experts are perfectly placed to adapt to the ever changing market conditions, giving our investors an 'out of the box' solution. Longevity is as much a focus as immediate success, ensuring you have the best options we can provide tomorrow as well as</p>
</section>
<div class="outline-btn about-cta">CONTACT US</div>

<section class="investments" role="img" aria-label="Blue chronograph watch on a dark sparkling background">
  <div class="investments-copy">
    <h2>INVESTMENTS</h2>
    <p>Interested in becoming part of the ever growing Solven Tride Portal?</p>
    <p>Please leave your details contact form below and one of the team will be in touch to discuss potential options.</p>
  </div>
  <div class="outline-btn invest-cta">LEARN MORE</div>
</section>

<h2 class="section-title sourcing-title">SOURCING YOUR WATCH</h2>
<div class="filter" style="left:121px;top:2085px">WATCH BRAND<svg viewBox="0 0 18 12"><path d="M2 2l7 7 7-7" fill="none" stroke="#222" stroke-width="2.4"/></svg></div>
<div class="filter" style="left:443px;top:2085px">YEAR<svg viewBox="0 0 18 12"><path d="M2 2l7 7 7-7" fill="none" stroke="#222" stroke-width="2.4"/></svg></div>
<div class="filter" style="left:767px;top:2085px">MATERIAL<svg viewBox="0 0 18 12"><path d="M2 2l7 7 7-7" fill="none" stroke="#222" stroke-width="2.4"/></svg></div>
<div class="filter" style="left:121px;top:2150px">BEZEL<svg viewBox="0 0 18 12"><path d="M2 2l7 7 7-7" fill="none" stroke="#222" stroke-width="2.4"/></svg></div>
<div class="filter" style="left:443px;top:2150px">STRAP<svg viewBox="0 0 18 12"><path d="M2 2l7 7 7-7" fill="none" stroke="#222" stroke-width="2.4"/></svg></div>
<div class="filter" style="left:767px;top:2150px">DESCRIPTION</div>
<div class="outline-btn source-cta">CONTACT US</div>

<section class="contact">
  <div class="contact-copy">
    <h2 class="section-title">CONTACT US</h2>
    <p class="intro">Alternatively please feel free to contact us on 01610004721</p>
    <p>For a more detailed chat with one of our timepiece specialists</p>
  </div>
  <div class="info-row" style="top:292px">
    <div class="ic"><svg width="22" height="26" viewBox="0 0 22 26"><path d="M11 1a9 9 0 0 0-9 9c0 7 9 15 9 15s9-8 9-15a9 9 0 0 0-9-9z" fill="#fff"/><circle cx="11" cy="10" r="3.5" fill="#c29d3d"/></svg></div>
    <div><b>Address :-</b><span>TBC</span></div>
  </div>
  <div class="info-row" style="top:378px">
    <div class="ic"><svg width="24" height="18" viewBox="0 0 24 18"><rect x="1" y="1" width="22" height="16" fill="#fff"/><path d="M1 1l11 9 11-9M1 17l8-7M23 17l-8-7" fill="none" stroke="#c29d3d" stroke-width="1.6"/></svg></div>
    <div><b>Email :-</b><span>hello@solventride-portal.example</span></div>
  </div>
  <div class="info-row" style="top:469px">
    <div class="ic"><svg width="22" height="22" viewBox="0 0 22 22"><path d="M5 1l4 5-2 3c1 3 3 5 6 6l3-2 5 4-3 4C10 20 2 12 1 4z" fill="#fff"/></svg></div>
    <div><b>Main Fax :-</b><span>01610004721</span></div>
  </div>
  <form class="contact-form">
    <div class="field" style="top:46px">First name*</div>
    <div class="field" style="top:108px">Last name</div>
    <div class="field" style="top:170px">Phone*</div>
    <div class="field" style="top:232px">Email address*</div>
    <div class="field" style="top:294px;height:156px">Message</div>
    <div class="outline-btn submit">SUBMIT NOW</div>
  </form>
</section>

<footer class="site-footer">
  <div class="footer-brand"><span class="brand-mark"></span>SOLVEN TRIDE PORTAL</div>
  <div class="socials"><span></span><span></span><span></span><span></span></div>
  <div class="divider" style="left:402px"></div>
  <div class="divider" style="left:644px"></div>
  <div class="divider" style="left:850px"></div>
  <div class="footer-col" style="left:402px">
    <h4>Navigation</h4>
    <ul><li>Home</li><li>About us</li><li>Investments</li><li>Search Watches</li><li>Contact us</li></ul>
  </div>
  <div class="footer-col" style="left:642px">
    <h4 style="font-size:14px">Other Links</h4>
    <ul><li style="color:#1e2a44">Terms &amp; Conditions</li><li style="color:#1e2a44">Prvacy Policy</li></ul>
  </div>
  <div class="footer-col" style="left:849px;border-left-width:3px;padding-left:24px">
    <h4 style="font-size:14px">Contact Information</h4>
  </div>
  <div class="fc-row" style="top:130px"><div class="ic"><svg width="14" height="17" viewBox="0 0 22 26"><path d="M11 1a9 9 0 0 0-9 9c0 7 9 15 9 15s9-8 9-15a9 9 0 0 0-9-9z" fill="#fff"/><circle cx="11" cy="10" r="3.5" fill="#c29d3d"/></svg></div>TBC</div>
  <div class="fc-row" style="top:174px"><div class="ic"><svg width="14" height="14" viewBox="0 0 22 22"><path d="M5 1l4 5-2 3c1 3 3 5 6 6l3-2 5 4-3 4C10 20 2 12 1 4z" fill="#fff"/></svg></div>+01610004721</div>
  <div class="fc-row" style="top:217px"><div class="ic"><svg width="15" height="11" viewBox="0 0 24 18"><rect x="1" y="1" width="22" height="16" fill="#fff"/><path d="M1 1l11 9 11-9" fill="none" stroke="#c29d3d" stroke-width="2"/></svg></div>hello@solventride-portal.example</div>
</footer>
<div class="copyright">© 2022 SOLVENTRIDE-PORTAL.EXAMPLE ALL RIGHT RESERVED</div>

</body>
</html>
```